CD front and back cover and CD disk. Front includes design elements of the attached band photo, the name of the band (Quiet Harbor Lanterns) and the album name (Paper Anchors?). I've attached a photshoped band photo and an original image. I like the color palette of the photoshoped pix but it may be too dark. So I've attached the original pix, that could be photoshoped. Music is alternative rock. See website qhlTunes.com and the EPK on the site. Songs are not up for this CD yet. Concept - modern, clean, NO gothic rock font or style of any kind.

Back cover needs songs, website and contact as follows:

Hold Ember (Electric)
Linger
Bent and Broken
Meridian
You Sink You Swim
Lean Past You
Hold Ember (Acoustic)
Room To Roam
The Tide
Push Too Far

qhlTunes.com
info@qhlTunes.com
- the actual cd needs the same as above
- use the DiscNook template Sleeve S240 

• Back cover needs the song titles, website, contact info and copyright as follows:
Hold Ember (electric)
Linger
Bent and Broken
Meridian
You Sink You Swim
Lean Past You
Hold Ember (acoustic)
Room To Roam
The Tide
Push Too Far

qhlTune.com
info@qhlTunes.com
Copyright © 2013 Quiet Harbor Lanterns | All Rights Reserved
Also - dimensions for CD Sleeve S240 on discnook.com
Also - CD disk to contain all of the above

```html
<!DOCTYPE html>
<html lang="en">
<head>
<meta charset="utf-8">
<title>Quiet Harbor Lanterns – Paper Anchors – Back Cover</title>
<link rel="stylesheet" href="https://fonts.googleapis.com/css2?family=Bebas+Neue&family=Oswald:wght@400;500&display=swap">
<style>
  :root {
    --edge-grey: #8e8e8e;
    --panel-dark: #141414;
    --panel-mid: #262626;
    --ink-white: #f2f2f2;
    --accent-orange: #f6a323;
    --label-paper: #f4f4f4;
    --label-ink: #111111;
  }
  html, body {
    margin: 0;
    padding: 0;
    overflow: hidden;
  }
  body {
    width: 1200px;
    height: 1091px;
    background: var(--edge-grey);
  }
  .back-cover {
    position: relative;
    width: 1200px;
    height: 1091px;
    overflow: hidden;
  }
  .cover-sheet {
    position: absolute;
    inset: 0;
  }
  .band-name {
    position: absolute;
    right: 30px;
    top: 40px;
    margin: 0;
    font-family: "Bebas Neue", "Oswald", sans-serif;
    font-weight: 400;
    font-size: 118px;
    line-height: 1;
    letter-spacing: 2px;
    color: var(--ink-white);
    text-transform: uppercase;
    white-space: nowrap;
  }
  .album-title {
    position: absolute;
    right: 30px;
    top: 168px;
    margin: 0;
    font-family: "Bebas Neue", "Oswald", sans-serif;
    font-weight: 400;
    font-size: 56px;
    line-height: 1;
    letter-spacing: 2px;
    color: var(--accent-orange);
    text-transform: uppercase;
    white-space: nowrap;
  }
  .track-list {
    position: absolute;
    left: 343px;
    top: 312px;
    margin: 0;
    padding: 0;
    list-style: none;
    font-family: "Oswald", sans-serif;
    font-weight: 400;
    font-size: 38px;
    line-height: 54.8px;
    letter-spacing: 1px;
    color: var(--ink-white);
    text-transform: uppercase;
  }
  .track-number {
    margin-right: 12px;
  }
  .contact-label {
    position: absolute;
    left: 338px;
    display: inline-block;
    padding: 0 12px;
    background: var(--label-paper);
    color: var(--label-ink);
    font-family: "Oswald", sans-serif;
    font-weight: 500;
    font-size: 28px;
    line-height: 44px;
    letter-spacing: 0.5px;
    text-transform: uppercase;
    clip-path: polygon(0 6%, 18% 0, 46% 4%, 72% 0, 100% 5%, 98% 48%, 100% 96%, 70% 100%, 40% 95%, 12% 100%, 1% 94%, 2% 50%);
  }
  .contact-site { top: 939px; }
  .contact-email { top: 1000px; }
</style>
</head>
<body>
  <main class="back-cover">
    <svg class="cover-sheet" width="1200" height="1091" viewBox="0 0 1200 1091" aria-hidden="true">
      <defs>
        <radialGradient id="sheetShade" cx="55%" cy="40%" r="75%">
          <stop offset="0%" stop-color="var(--panel-mid)"/>
          <stop offset="100%" stop-color="var(--panel-dark)"/>
        </radialGradient>
      </defs>
      <polygon fill="url(#sheetShade)" points="
        0,0 1200,0 1200,120 1193,220 1198,340 1190,460 1196,600 1188,720 1194,860 1186,980 1190,1070
        1100,1078 980,1072 860,1080 720,1074 600,1081 470,1073 340,1079 210,1072 90,1080 14,1074
        10,960 16,840 8,720 14,600 6,470 13,340 7,210 14,90 0,0"/>
    </svg>

    <h1 class="band-name">Quiet Harbor Lanterns</h1>
    <h2 class="album-title">Paper Anchors</h2>

    <ol class="track-list">
      <li><span class="track-number">01.</span>Hold Ember (Electric)</li>
      <li><span class="track-number">02.</span>Linger</li>
      <li><span class="track-number">03.</span>Bent and Broken</li>
      <li><span class="track-number">04.</span>Meridian</li>
      <li><span class="track-number">05.</span>You Sink You Swim</li>
      <li><span class="track-number">06.</span>Lean Past You</li>
      <li><span class="track-number">07.</span>Hold Ember (Acoustic)</li>
      <li><span class="track-number">08.</span>Room To Roam</li>
      <li><span class="track-number">09.</span>The Tide</li>
      <li><span class="track-number">10.</span>Push Too Far</li>
    </ol>

    <span class="contact-label contact-site">qhlTunes.com</span>
    <span class="contact-label contact-email">info@qhlTunes.com</span>
  </main>
</body>
</html>
```